Professional Business Card for Commercial Cleaning Company

We need a business card that represents our commercial janitorial cleaning company and represent several brands for our company so we do not want to highlight the logo too much. We want something that says we are professional.
Notes:No website or address as we have many locations and many websites and companies under our corporate name of "Brightvale Holdings, LLC" . Every time we hand a customer a business card they have contacted us via another brand we own but we don't want to have 21 business cards so we want to not focus on Brightvale Holdings, LLC too much since people will automatically ask "What is Brightvale Holdings, LLC" Example: Noodle Barn and Wrap Lantern restaurants are owned by "Zest! Brands" is the corporation name. Same principle here. Except we do not advertise at this time that all of our brands are connected. Hope this helps.
Target Market(s)
Commercial Cleaning
Industry/Entity Type
Janitorial Service
Contact Information for Business Card
Milo Jarvis
Business Development
555-382-9047
sales@brightvaleholdingsllc.example
Requirements
Must have
- Logo with contact information, need to be able to easily edit contact info for others in my office.
Nice to have
- Professional Image. Like to see a colorful bold look and a more standard business card look.
Should not have
- Any type of cleaning icons, tools, people or water.

```html
<!DOCTYPE html>
<html lang="en">
<head>
<meta charset="utf-8">
<title>Brightvale Holdings, LLC — Business Card</title>
<link href="https://fonts.googleapis.com/css2?family=Montserrat:wght@400;500;600;700&display=swap" rel="stylesheet">
<style>
  :root {
    --navy: #1d3f7c;
    --green: #5c9e3a;
    --paper: #ffffff;
    --ink: #1a1a1a;
    --backdrop: #e9e7e3;
  }
  * { box-sizing: border-box; margin: 0; padding: 0; }
  html, body { width: 1200px; height: 900px; overflow: hidden; }
  body {
    background: var(--backdrop);
    font-family: "Montserrat", sans-serif;
    display: flex;
    flex-direction: column;
    align-items: center;
    justify-content: center;
    gap: 36px;
  }
  .card {
    position: relative;
    width: 700px;
    height: 400px;
    background: var(--paper);
    box-shadow: 0 6px 18px rgba(0,0,0,0.12);
    overflow: hidden;
  }
  /* Logo side */
  .card--logo .band-navy {
    position: absolute; left: 0; top: 0; bottom: 0; width: 80px;
    background: var(--navy);
  }
  .card--logo .band-green {
    position: absolute; left: 80px; top: 0; bottom: 0; width: 22px;
    background: var(--green);
  }
  .card--logo .brand {
    position: absolute; left: 102px; right: 0; top: 0; bottom: 0;
    display: flex; align-items: center; justify-content: center;
  }
  .brand-name {
    color: var(--navy);
    font-weight: 600;
    font-size: 30px;
    letter-spacing: 0.2px;
    white-space: nowrap;
  }
  /* Contact side */
  .card--contact .brand {
    position: absolute; left: 0; right: 0; top: 92px;
    text-align: center;
  }
  .card--contact .brand-name { font-size: 28px; }
  .person {
    position: absolute; left: 0; right: 0; top: 158px;
    text-align: center;
  }
  .person-name {
    font-weight: 700;
    font-size: 38px;
    letter-spacing: 9px;
    color: var(--ink);
  }
  .person-title {
    margin-top: 10px;
    font-weight: 500;
    font-size: 14px;
    letter-spacing: 2px;
    color: var(--ink);
  }
  .footer-navy {
    position: absolute; left: 0; bottom: 0; width: 112px; height: 74px;
    background: var(--navy);
  }
  .footer-green {
    position: absolute; left: 120px; right: 0; bottom: 0; height: 74px;
    background: var(--green);
    display: flex; align-items: center; gap: 20px;
    padding: 0 18px 0 22px;
    color: #fff;
    overflow: hidden;
  }
  .contact-item {
    display: flex; align-items: center; gap: 10px;
    font-weight: 500; font-size: 14px; letter-spacing: 1.6px;
    white-space: nowrap;
  }
  .contact-item--email { font-size: 13px; letter-spacing: 0.9px; }
  .icon-badge {
    width: 22px; height: 22px; border-radius: 50%;
    background: #fff;
    display: flex; align-items: center; justify-content: center;
    flex: none;
  }
  .icon-badge svg { width: 13px; height: 13px; }
  .icon-at { color: var(--green); font-weight: 700; font-size: 13px; letter-spacing: 0; line-height: 1; }
</style>
</head>
<body>
  <section class="card card--logo" aria-label="Business card, logo side">
    <div class="band-navy"></div>
    <div class="band-green"></div>
    <div class="brand"><span class="brand-name">Brightvale Holdings, LLC</span></div>
  </section>

  <section class="card card--contact" aria-label="Business card, contact side">
    <div class="brand"><span class="brand-name">Brightvale Holdings, LLC</span></div>
    <div class="person">
      <p class="person-name">Milo Jarvis</p>
      <p class="person-title">Business Development</p>
    </div>
    <div class="footer-navy"></div>
    <div class="footer-green">
      <span class="contact-item">
        <span class="icon-badge">
          <svg viewBox="0 0 24 24" aria-hidden="true"><path fill="#5c9e3a" d="M6.6 10.8a15.1 15.1 0 0 0 6.6 6.6l2.2-2.2a1 1 0 0 1 1-.25 11.4 11.4 0 0 0 3.6.57 1 1 0 0 1 1 1V20a1 1 0 0 1-1 1A17 17 0 0 1 3 4a1 1 0 0 1 1-1h3.5a1 1 0 0 1 1 1c0 1.25.2 2.450.57 3.57a1 1 0 0 1-.25 1z"/></svg>
        </span>
        555-382-9047
      </span>
      <span class="contact-item contact-item--email">
        <span class="icon-badge"><span class="icon-at">@</span></span>
        sales@brightvaleholdingsllc.example
      </span>
    </div>
  </section>
</body>
</html>
```